Kestrel Photography Business Card

I need a business card designed for a photography business based in Perth, Western Australia called Kestrel Photography.

We specialise in wedding, event photography and portrait photography.

The business card must borrow the style of the attached logo.

The hex codes for the colours in the logo are:
#ED1D85 - Pink
#89C23E - Green
#37282F - Black

The name on the card will be:
Name: Toviran
Phone: 0417395268
Website: www.kestrelphotography.com.au
Facebook: kestrelphotography

I am open and happy to accept creative concepts.

I’d like some space at the back for writing notes and appointment details.

```html
<!DOCTYPE html>
<html lang="en">
<head>
<meta charset="utf-8">
<title>Kestrel Photography Business Card</title>
<link href="https://fonts.googleapis.com/css2?family=Open+Sans:wght@400;600;700&display=swap" rel="stylesheet">
<style>
  :root {
    --pink: #ED1D85;
    --green: #89C23E;
    --ink: #37282F;
    --rule: #b9b9b9;
    --paper: #ffffff;
    --stage: #e9e9ee;
  }
  * { box-sizing: border-box; margin: 0; padding: 0; }
  html, body { width: 1200px; height: 987px; overflow: hidden; }
  body {
    background: var(--stage);
    font-family: "Open Sans", Arial, sans-serif;
    position: relative;
  }
  .card {
    position: absolute;
    width: 580px;
    height: 330px;
    background: var(--paper);
    border-radius: 26px;
    overflow: hidden;
    box-shadow: 0 6px 18px rgba(0,0,0,0.12);
  }
  .card--back { left: 580px; top: 110px; }
  .card--front { left: 40px; top: 520px; }

  .brand {
    position: absolute;
    display: flex;
    align-items: center;
    gap: 16px;
  }
  .brand__mark {
    width: 56px; height: 56px;
    flex: none;
    border-radius: 50%;
    background: radial-gradient(circle, var(--paper) 38%, var(--green) 40%, var(--green) 52%, var(--pink) 54%);
  }
  .brand__name {
    font-size: 13px;
    font-weight: 400;
    letter-spacing: 9px;
    color: var(--ink);
    text-transform: uppercase;
    white-space: nowrap;
  }
  .card--front .brand { left: 90px; top: 36px; }
  .card--back .brand { right: 40px; top: 20px; }

  .notes__label {
    position: absolute; left: 40px; top: 96px;
    font-size: 18px; line-height: 24px; color: #111;
  }
  .notes__line {
    position: absolute; height: 1px; background: var(--rule);
  }
  .back__web {
    position: absolute; left: 40px; bottom: 28px;
    font-size: 17px; letter-spacing: 1px; color: var(--ink);
  }

  .holder {
    position: absolute; left: 40px; top: 108px;
    font-size: 22px; font-weight: 700; color: var(--pink);
    text-transform: uppercase;
  }
  .wave { position: absolute; left: 0; top: 0; width: 580px; height: 330px; }
  .contacts {
    position: absolute; right: 30px; bottom: 16px;
    list-style: none;
    color: var(--paper); font-size: 17px;
  }
  .contacts li { display: flex; align-items: center; justify-content: flex-end; gap: 8px; line-height: 26px; }
  .contacts svg { width: 16px; height: 16px; flex: none; }
  .social-dot { width: 14px; height: 14px; border: 2px solid var(--paper); border-radius: 3px; flex: none; }
</style>
</head>
<body>

  <section class="card card--back" aria-label="Card back">
    <div class="brand">
      <span class="brand__name">Kestrel Photography</span>
      <span class="brand__mark" aria-hidden="true"></span>
    </div>
    <p class="notes__label">notes:</p>
    <span class="notes__line" style="left:98px;top:118px;width:442px"></span>
    <span class="notes__line" style="left:40px;top:160px;width:500px"></span>
    <span class="notes__line" style="left:40px;top:202px;width:500px"></span>
    <span class="notes__line" style="left:40px;top:244px;width:500px"></span>
    <p class="back__web">www.kestrelphotography.com.au</p>
  </section>

  <section class="card card--front" aria-label="Card front">
    <svg class="wave" viewBox="0 0 580 330" aria-hidden="true">
      <path d="M0 130 C30 230 250 195 580 205 L580 330 L0 330 Z" fill="var(--pink)"/>
      <path d="M22 160 C55 240 260 210 580 220" fill="none" stroke="var(--paper)" stroke-width="4"/>
    </svg>
    <div class="brand">
      <span class="brand__name">Kestrel Photography</span>
      <span class="brand__mark" aria-hidden="true"></span>
    </div>
    <p class="holder">Toviran</p>
    <ul class="contacts">
      <li>
        <svg viewBox="0 0 16 16" aria-hidden="true"><circle cx="8" cy="8" r="7" fill="none" stroke="#fff" stroke-width="1.5"/><path d="M5 4 L7 4 L7.5 6 L6.5 7 C7 8.5 8 9.5 9 10 L10 9 L12 9.5 L12 11.5 C8 12 4.5 8 5 4 Z" fill="#fff"/></svg>
        0417395268
      </li>
      <li><span class="social-dot" aria-hidden="true"></span>kestrelphotography</li>
      <li>
        <svg viewBox="0 0 16 16" aria-hidden="true"><circle cx="8" cy="8" r="7" fill="none" stroke="#fff" stroke-width="1.3"/><ellipse cx="8" cy="8" rx="3" ry="7" fill="none" stroke="#fff" stroke-width="1"/><path d="M1 8 H15" stroke="#fff" stroke-width="1"/></svg>
        www.kestrelphotography.com.au
      </li>
    </ul>
  </section>

</body>
</html>
```